Scrum Master & Agile IT Coach Needing Business Website

Hello, my name is Brent Ellison
I am a project manger, scrum master, & agile coach. I work with IT development teams on major projects for Fortune 500 companies . My project management business has a website and can be found here: www.tq-steadfast.example

I have launched a new company, ALL focused on IT Agile Coaching, I am looking to have a website created for my new company - the name of the new company is: Pins and Pegs - Agile IT Coaching and Training.
I have a logo and it is provided in the materials. I like to logo; I am open to different color pallets.

The website will have a total of 7 pages; I have content for 5 of the 7 pages prepared; the other 2 pages will say under construction.

Page 1 Who am I, What I do, My Experience
Demonstrated experience and progression from Scrum Master to
Program Manager to Coach

Page 2 Pins & Pegs - Agile Team Coaching
teams working major IT projects, multiple months/years

Page 3 Coaching @ the Team Level

Page 4 Coaching @ the Program Level ; LeanScale ART level

Pages 5 -6 Under Construction

Page 7 Presentations, Slide Decks, Reference Materials

Mentors Nook need to have this highlighted somewhere Monthly Blog
Updates

Industry/Entity Type

IT development

Coding

Coded - Design and coding required

Number of Pages Required

5+ page

Requirements
Must have
• the website must be bold - I want those who visit to remember coming to my coaching site
Nice to have
• nice to have will be a modern / futuristic website; I work with IT developers, I want a website they will like
Should not have
• should not be stiff - it should be professional but fun

```html
<!DOCTYPE html>
<html lang="en">
<head>
<meta charset="utf-8">
<title>Pins & Pegs - Agile IT Coaching and Training</title>
<link href="https://fonts.googleapis.com/css2?family=Oswald:wght@500;600&family=Poppins:ital,wght@0,400;0,500;0,600;1,400;1,500&display=swap" rel="stylesheet">
<style>
:root{
  --green:#18c98c;
  --ink:#1d1f24;
  --text:#3c3f45;
  --muted:#6f737a;
  --navy:#1b3e63;
  --hero-a:#061a22;
  --hero-b:#0f3d48;
  --hero-c:#2a7c86;
  --band:#dcdcdc;
  --badge:#e4e6e8;
  --soft:#f4f4f4;
  --footer:#202020;
  --white:#ffffff;
}
*{box-sizing:border-box;margin:0;padding:0}
html,body{width:1200px;height:5240px;overflow:hidden}
body{position:relative;background:var(--white);font-family:'Poppins',sans-serif;color:var(--text)}
.abs{position:absolute}
.display{font-family:'Oswald',sans-serif;font-weight:600;text-transform:uppercase;color:var(--ink);letter-spacing:.5px}
.eyebrow{font-size:16px;font-weight:500;color:var(--green);text-transform:uppercase;letter-spacing:.5px}

/* header */
.site-header{left:0;top:0;width:1200px;height:106px;background:var(--white);z-index:3}
.brand{left:85px;top:24px;display:flex;align-items:center;gap:14px}
.brand-mark{width:52px;height:52px;border:3px solid var(--navy);border-radius:4px}
.brand-name{font-family:'Poppins',sans-serif;font-weight:600;font-size:40px;color:var(--navy);line-height:1}
.main-nav a{position:absolute;top:32px;font-size:15px;line-height:19px;color:var(--ink);text-decoration:none}

/* hero */
.hero{left:0;top:106px;width:1200px;height:667px;clip-path:polygon(0 0,100% 0,100% 504px,0 667px);
  background:linear-gradient(100deg,var(--hero-a) 0%,var(--hero-b) 45%,var(--hero-c) 70%,#173d4d 100%)}
.hero-media{right:0;top:0;width:640px;height:667px;background:radial-gradient(ellipse at 60% 40%,rgba(70,210,220,.35),transparent 60%)}
.hero-eyebrow{left:112px;top:112px;font-size:21px;color:var(--green)}
.hero-title{left:112px;top:168px;font-family:'Oswald',sans-serif;font-weight:500;font-size:45px;line-height:57px;color:var(--white);text-transform:uppercase;white-space:nowrap}
.btn-primary{left:112px;top:433px;width:195px;height:65px;background:var(--green);color:var(--white);font-size:18px;font-weight:500;display:flex;align-items:center;justify-content:center;text-transform:uppercase}

/* about */
.about-frame{left:92px;top:814px;width:457px;height:504px;border:3px solid var(--green)}
.about-photo{left:112px;top:830px;width:425px;height:472px;background:linear-gradient(135deg,#c7b9a6,#8b6f55 55%,#4a3a2d)}
.about-eyebrow{left:614px;top:828px}
.about-name{left:614px;top:864px;font-size:44px}
.about-role{left:614px;top:934px;font-size:18px;font-style:italic;font-weight:500;color:var(--text)}
.about-copy{left:614px;width:480px;font-size:15px;line-height:24.5px;color:var(--muted)}

/* designations */
.designations{left:112px;top:1379px;width:976px;height:61px;background:var(--band);display:flex;align-items:center;justify-content:center;font-size:25px;font-weight:500;color:var(--ink)}
.designations-pointer{left:572px;top:1440px;width:0;height:0;border-left:28px solid transparent;border-right:28px solid transparent;border-top:28px solid var(--band)}
.badge{top:1503px;width:150px;height:150px;border-radius:50%;background:var(--badge)}
.badge-links .link-btn{position:absolute;top:1709px;height:65px;border:2px solid #9a9a9a;display:flex;align-items:center;justify-content:center;text-align:center;font-size:17px;font-weight:500;color:var(--ink);text-transform:uppercase;line-height:20px}
.badge-links .link-btn.active{background:var(--green);border-color:var(--green);color:var(--white)}

/* roles */
.roles{left:0;top:1810px;width:1200px;height:620px;clip-path:polygon(0 122px,100% 0,100% 530px,0 620px);
  background:linear-gradient(90deg,#2e6068 0%,#4f8188 35%,#7fa3a8 55%,#3f5f66 72%,#b9cccf 88%,#dfe7e8 100%)}
.roles-eyebrow{left:173px;top:2012px}
.roles-title{left:173px;top:2046px;font-size:42px;color:var(--white);font-weight:500}
.roles-list{left:173px;top:2132px;list-style:none;display:flex;flex-direction:column;gap:16px}
.roles-list li{display:flex;align-items:center;gap:10px;font-size:18px;color:var(--white);height:29px}

/* experience */
.exp-eyebrow{left:0;width:1200px;text-align:center;top:2472px}
.exp-title{left:0;width:1200px;text-align:center;top:2506px;font-size:42px;font-weight:500}
.exp-card{left:112px;width:976px;background:var(--white);box-shadow:0 4px 22px rgba(0,0,0,.10);display:flex}
.exp-media{width:451px;height:100%}
.exp-body{flex:1;padding:26px 22px 0 48px}
.exp-body h3{font-size:24px;font-weight:500;color:var(--ink);line-height:31px;margin-bottom:22px}
.ticks{list-style:none;display:flex;flex-direction:column;gap:19px}
.ticks li{display:flex;gap:10px;font-size:15px;line-height:18px;color:var(--text)}
.ticks svg{flex:none;margin-top:1px}
.exp-card.is-green .exp-body{background:var(--green);padding-left:48px}
.exp-card.is-green h3,.exp-card.is-green .ticks li{color:var(--white)}

/* blog */
.blog-bg{left:0;top:4070px;width:1200px;height:761px;background:var(--soft);clip-path:polygon(0 84px,100% 0,100% 100%,0 100%)}
.blog-eyebrow{left:0;width:1200px;text-align:center;top:4176px}
.blog-title{left:0;width:1200px;text-align:center;top:4212px;font-size:42px;font-weight:500}
.post{top:4302px;width:312px;height:413px;background:var(--white);box-shadow:0 3px 14px rgba(0,0,0,.07)}
.post-media{width:100%;height:193px}
.post-body{padding:24px 20px 0 20px}
.post-body h4{font-size:19px;font-weight:500;color:var(--ink);line-height:24px}
.post-date{display:flex;align-items:center;gap:6px;font-size:15px;color:var(--ink);margin-top:8px}
.post-body p{font-size:14.5px;line-height:26px;color:var(--muted);margin-top:10px}
.read-more{display:block;font-size:15px;font-weight:500;color:var(--green);text-transform:uppercase;margin-top:14px}

/* footer */
.site-footer{left:0;top:4831px;width:1200px;height:409px;background:var(--footer)}
.footer-brand{left:106px;top:4915px;display:flex;align-items:center;gap:16px}
.footer-brand .brand-mark{border-color:var(--white)}
.footer-brand .brand-name{color:var(--white);font-size:42px}
.footer-head{top:4852px;font-size:17px;font-weight:500;color:var(--white)}
.footer-links{left:543px;top:4898px;list-style:none;width:300px}
.footer-links li{font-size:15px;line-height:18px;color:var(--white);margin-bottom:19px}
.footer-contact{left:848px;top:4898px;list-style:none}
.footer-contact li{display:flex;align-items:center;gap:8px;font-size:15px;color:var(--white);height:18px;margin-bottom:19px}
.footer-rule{left:0;top:5152px;width:1200px;height:1px;background:#3a3a3a}
.copyright{left:112px;top:5180px;font-size:15px;color:var(--white)}
.social{top:5169px;width:44px;height:44px;border:2px solid var(--green);border-radius:50%}
</style>
</head>
<body>
<svg width="0" height="0" style="position:absolute" aria-hidden="true">
  <defs>
    <symbol id="tick" viewBox="0 0 16 16"><circle cx="8" cy="8" r="8" fill="currentColor"/><path d="M4.5 8.3l2.3 2.3 4.7-4.9" fill="none" stroke="#fff" stroke-width="2" stroke-linecap="round" stroke-linejoin="round"/></symbol>
    <symbol id="tick-inv" viewBox="0 0 16 16"><circle cx="8" cy="8" r="8" fill="#fff"/><path d="M4.5 8.3l2.3 2.3 4.7-4.9" fill="none" stroke="#18c98c" stroke-width="2" stroke-linecap="round" stroke-linejoin="round"/></symbol>
    <symbol id="calendar" viewBox="0 0 16 16"><rect x="1.5" y="3" width="13" height="11.5" rx="1.5" fill="none" stroke="#18c98c" stroke-width="1.6"/><path d="M1.5 6.5h13M5 1.5v3M11 1.5v3" stroke="#18c98c" stroke-width="1.6"/></symbol>
  </defs>
</svg>

<header class="abs site-header">
  <div class="abs brand"><span class="brand-mark"></span><span class="brand-name">Pins &amp; Pegs</span></div>
  <nav class="main-nav">
    <a style="left:490px">Agile<br>Coaching</a>
    <a style="left:594px">Coaching @<br>the Team Level</a>
    <a style="left:742px">Coaching @<br>the Program Level</a>
    <a style="left:915px">Mentors<br>Nook</a>
    <a style="left:1013px">Reference<br>Materials</a>
  </nav>
</header>

<section class="abs hero">
  <div class="abs hero-media" role="img" aria-label="Hands typing on a laptop with a glowing project timeline chart"></div>
  <p class="abs hero-eyebrow">Pins and Pegs - Agile IT Coaching and Training</p>
  <h1 class="abs hero-title">Demonstrate experience<br>and progression from<br>Scrum Master to program<br>manager to coach</h1>
  <a class="abs btn-primary">Get in touch</a>
</section>

<section>
  <div class="abs about-frame"></div>
  <div class="abs about-photo" role="img" aria-label="Portrait of Brent Ellison"></div>
  <p class="abs eyebrow about-eyebrow">About me</p>
  <h2 class="abs display about-name">Brent Ellison</h2>
  <p class="abs about-role">Senior Scrum Master &amp; Team Agile Coach</p>
  <p class="abs about-copy" style="top:983px">Brent brings 13+ years of experience to his clients – experience which encompasses various project management methodologies ranging from waterfall, agile, and mixed hybrid frameworks.</p>
  <p class="abs about-copy" style="top:1106px">A separating factor in the consultancy services provided at Tranquil Steadfast Consulting, LLC is that Brent has spent years on both the Business and IT/IS sides of the project management business. Brent understands the process of driving business priorities and objectives from ideation to production while also understanding the intricacies of software development and team cadence.</p>
</section>

<section>
  <div class="abs designations">Coaching Designations</div>
  <div class="abs designations-pointer"></div>
  <div class="abs badge" style="left:110px" role="img" aria-label="Coaching certification badge"></div>
  <div class="abs badge" style="left:308px" role="img" aria-label="Educator certification badge"></div>
  <div class="abs badge" style="left:516px" role="img" aria-label="Scrum Master certification badge"></div>
  <div class="abs badge" style="left:715px" role="img" aria-label="Scaled agile Scrum Master certification badge"></div>
  <div class="abs badge" style="left:917px" role="img" aria-label="Advanced Scrum Master certification badge"></div>
  <div class="badge-links">
    <a class="link-btn" style="left:307px;width:216px">Agile Guild</a>
    <a class="link-btn active" style="left:535px;width:130px">Badgely</a>
    <a class="link-btn" style="left:677px;width:214px">Scaled Delivery<br>Institute</a>
  </div>
</section>

<section>
  <div class="abs roles" role="img" aria-label="Businessman in a suit overlooking a city skyline"></div>
  <p class="abs eyebrow roles-eyebrow">What I do</p>
  <h2 class="abs display roles-title">Roles I have held</h2>
  <ul class="abs roles-list">
    <li><svg width="16" height="16" style="color:var(--green)"><use href="#tick"/></svg>Sr. Scrum Master</li>
    <li><svg width="16" height="16" style="color:var(--green)"><use href="#tick"/></svg>Advanced LeanScale Scrum Master</li>
    <li><svg width="16" height="16" style="color:var(--green)"><use href="#tick"/></svg>Hybrid Scrum Master/ Project Manager</li>
    <li><svg width="16" height="16" style="color:var(--green)"><use href="#tick"/></svg>Business (Finance Transformation Program Manager</li>
  </ul>
</section>

<section>
  <p class="abs eyebrow exp-eyebrow">Experience</p>
  <h2 class="abs display exp-title">What is my experience</h2>

  <article class="abs exp-card" style="top:2610px;height:437px">
    <div class="exp-media" role="img" aria-label="Hand writing on a whiteboard covered with sticky notes" style="background:linear-gradient(135deg,#e9eef3,#c9d6e2 50%,#f3d76a)"></div>
    <div class="exp-body">
      <h3>As a LeanScale Adv Scrum Master, I:</h3>
      <ul class="ticks" style="color:var(--green)">
        <li><svg width="16" height="16"><use href="#tick"/></svg>stand up teams</li>
        <li><svg width="16" height="16"><use href="#tick"/></svg>run development efforts concurrently leading multiple teams</li>
        <li><svg width="16" height="16"><use href="#tick"/></svg>run LeanScale ceremonies</li>
        <li><svg width="16" height="16"><use href="#tick"/></svg>Scrum of Scrums facilitator</li>
        <li><svg width="16" height="16"><use href="#tick"/></svg>PI Planning team facilitator (multiple teams on ART)</li>
        <li><svg width="16" height="16"><use href="#tick"/></svg>Teach and coach to advanced development team strategies</li>
        <li><svg width="16" height="16"><use href="#tick"/></svg>Lead program level communications and business status updates on behalf of the team</li>
      </ul>
    </div>
  </article>

  <article class="abs exp-card is-green" style="top:3098px;height:421px">
    <div class="exp-body" style="padding-right:40px">
      <h3>As a Hybrid Scrum Master /<br>Project Manager, I:</h3>
      <ul class="ticks">
        <li><svg width="16" height="16"><use href="#tick-inv"/></svg>standup teams</li>
        <li><svg width="16" height="16"><use href="#tick-inv"/></svg>run multiple program level projects simultaneously</li>
        <li><svg width="16" height="16"><use href="#tick-inv"/></svg>implement custom hybrid development strategies</li>
        <li><svg width="16" height="16"><use href="#tick-inv"/></svg>manage to project triple constraints</li>
        <li><svg width="16" height="16"><use href="#tick-inv"/></svg>communications lead and business liaison</li>
        <li><svg width="16" height="16"><use href="#tick-inv"/></svg>use multiple coaching styles based on team and project</li>
      </ul>
    </div>
    <div class="exp-media" role="img" aria-label="Team of colleagues gathered around a laptop" style="background:linear-gradient(135deg,#8a6a52,#c69a74 45%,#3d4f5f)"></div>
  </article>

  <article class="abs exp-card" style="top:3572px;height:439px">
    <div class="exp-media" role="img" aria-label="Hand placing a lightbulb block on a pyramid of wooden blocks" style="background:linear-gradient(180deg,#2f6f86,#6a9aa8 45%,#a77a4e 80%,#6e4a2c)"></div>
    <div class="exp-body">
      <h3>Business Transformation<br>Program Manager</h3>
      <ul class="ticks" style="color:var(--green)">
        <li><svg width="16" height="16"><use href="#tick"/></svg>lead business transformation efforts at the program level</li>
        <li><svg width="16" height="16"><use href="#tick"/></svg>work with multiple product owners, business analysts, and business stakeholders on requirements</li>
        <li><svg width="16" height="16"><use href="#tick"/></svg>lead the international rollout, onboarding, and support of new transformational CRM tool, Cloudtrack</li>
        <li><svg width="16" height="16"><use href="#tick"/></svg>standup and lead multi-functional teams consisting of business and technology team members</li>
        <li><svg width="16" height="16"><use href="#tick"/></svg>Serve as program organization and communications lead</li>
      </ul>
    </div>
  </article>
</section>

<section>
  <div class="abs blog-bg"></div>
  <p class="abs eyebrow blog-eyebrow">Blog</p>
  <h2 class="abs display blog-title">Mentors Nook</h2>

  <article class="abs post" style="left:112px">
    <div class="post-media" role="img" aria-label="Colleagues discussing work in an office" style="background:linear-gradient(135deg,#5b4636,#b08d6e 50%,#e8e2d8)"></div>
    <div class="post-body">
      <h4>Lorem ipsum dolor sit ame</h4>
      <p class="post-date"><svg width="15" height="15"><use href="#calendar"/></svg>16/11/2022</p>
      <p>Duis aute irure dolor in repreerit in voluptate velit esse.</p>
      <a class="read-more">Read more</a>
    </div>
  </article>
  <article class="abs post" style="left:443px">
    <div class="post-media" role="img" aria-label="Hand touching a rising digital chart" style="background:linear-gradient(135deg,#0c2a4a,#1f5a8c 55%,#7fb3db)"></div>
    <div class="post-body">
      <h4>Lorem ipsum dolor sit ame</h4>
      <p class="post-date"><svg width="15" height="15"><use href="#calendar"/></svg>16/11/2022</p>
      <p>Duis aute irure dolor in repreerit in voluptate velit esse.</p>
      <a class="read-more">Read more</a>
    </div>
  </article>
  <article class="abs post" style="left:777px">
    <div class="post-media" role="img" aria-label="Red game piece lifted above a row of wooden pieces" style="background:linear-gradient(90deg,#ffffff,#efe7df 50%,#cfae8a)"></div>
    <div class="post-body">
      <h4>Lorem ipsum dolor sit ame</h4>
      <p class="post-date"><svg width="15" height="15"><use href="#calendar"/></svg>16/11/2022</p>
      <p>Duis aute irure dolor in repreerit in voluptate velit esse.</p>
      <a class="read-more">Read more</a>
    </div>
  </article>
</section>

<footer class="abs site-footer"></footer>
<div class="abs footer-brand"><span class="brand-mark"></span><span class="brand-name">Pins &amp; Pegs</span></div>
<p class="abs footer-head" style="left:543px">Quick Links</p>
<ul class="abs footer-links">
  <li>Home</li>
  <li>Agile Team Coaching</li>
  <li>Coaching @ the Team Level</li>
  <li>Coaching @ the Program Level ;<br>LeanScale ART level</li>
  <li>Mentors Nook</li>
  <li>Contact</li>
</ul>
<p class="abs footer-head" style="left:848px">Contact Us</p>
<ul class="abs footer-contact">
  <li><svg width="14" height="14" viewBox="0 0 16 16"><path d="M3.6 1.5l2.6 2.6-1.5 2.1a9 9 0 0 0 5.1 5.1l2.1-1.5 2.6 2.6-1.7 2.1C7 14 2 9 1.5 3.2z" fill="#18c98c"/></svg>1 555 010 0199</li>
  <li><svg width="14" height="14" viewBox="0 0 16 16"><rect x="1" y="3" width="14" height="10" rx="1" fill="#18c98c"/><path d="M1.5 4l6.5 5 6.5-5" fill="none" stroke="#202020" stroke-width="1.4"/></svg>brent.ellison@pinsandpegs.example</li>
  <li><svg width="14" height="14" viewBox="0 0 16 16"><path d="M8 1a5 5 0 0 0-5 5c0 4 5 9 5 9s5-5 5-9a5 5 0 0 0-5-5z" fill="#18c98c"/><circle cx="8" cy="6" r="1.8" fill="#202020"/></svg>Remote Location</li>
</ul>
<div class="abs footer-rule"></div>
<p class="abs copyright">Copyright © 2022 Pins and Pegs - Agile IT Coaching and Training - all rights reserved.</p>
<span class="abs social" style="left:940px" aria-label="Social profile"></span>
<span class="abs social" style="left:991px" aria-label="Social profile"></span>
<span class="abs social" style="left:1042px" aria-label="Social profile"></span>
</body>
</html>
```